School Hallway Magnetic Display Design for school values

I am looking for a someone to help me design a magnetic hallway display that will hang in the hallway of our small school. There are several elements, including 1. 6ft by 4ft designed magnetic bulletin board, 2. Magnets that will stick to the board. See attachment for which elements belong where. The display will be for our TAVRON program, which rewards students for demonstrating our school values. We want the display to be beautiful and interactive. We are also rebranding, so we want the design to align with our new fonts and colors. In the attached PDF is an outline of our new brand guidelines. Unfortunately, we don't have the color codes, but I'm hoping that you can match the colors listed. Attached are elements to be used on the board, but please use your creativity to make it more dynamic and visually appealing. For example, the star magnets could be another shape. The TAVRON magnets must remain the same. I've included two photos of boards at other schools that inspired this project.

Target Market(s)

School Community

Industry/Entity Type

Education

Requirements
Should not have
• School Logo

```html
<!DOCTYPE html>
<html lang="en">
<head>
<meta charset="utf-8">
<title>TAVRON of the Month – Hallway Display</title>
<link href="https://fonts.googleapis.com/css2?family=Playfair+Display:wght@800&family=Roboto:wght@400&display=swap" rel="stylesheet">
<style>
  :root {
    --bg: #e6e6e6;
    --navy: #204a72;
    --blue-dark: #2c5d95;
    --blue-light: #afcce3;
    --yellow: #fddb7f;
    --coral: #de8a75;
    --cream: #fdf7ea;
    --white: #ffffff;
    --shadow: #b3b3b3;
    --note: #e3262a;
  }
  * { margin: 0; padding: 0; box-sizing: border-box; }
  html, body { width: 1087px; height: 1200px; overflow: hidden; }
  body { background: var(--bg); position: relative; font-family: "Playfair Display", serif; }

  .board {
    position: absolute; left: 69px; top: 154px; width: 949px; height: 686px;
    background: var(--white);
    box-shadow: 7px 7px 0 var(--shadow);
  }
  .board-frame {
    position: absolute; inset: 0;
    border: 52px solid transparent;
    background: linear-gradient(135deg, var(--blue-light), var(--blue-dark) 45%, var(--blue-light) 70%, var(--yellow)) border-box;
    -webkit-mask: linear-gradient(#000 0 0) padding-box, linear-gradient(#000 0 0);
    -webkit-mask-composite: xor;
    mask: linear-gradient(#000 0 0) padding-box exclude, linear-gradient(#000 0 0);
  }
  .title-field {
    position: absolute; left: 52px; top: 0; width: 264px; height: 53px;
    background: var(--white);
  }
  .board-title {
    position: absolute; left: 77px; top: 6px;
    color: var(--navy); font-weight: 800; line-height: 1;
  }
  .board-title .name { display: block; font-size: 60px; letter-spacing: -1px; }
  .board-title .sub { display: block; font-size: 29px; margin-top: -2px; letter-spacing: 0.2px; }

  .thermometer {
    position: absolute; left: 751px; top: 117px; width: 116px; height: 469px;
    background: linear-gradient(180deg, var(--blue-light), var(--blue-light) 80%, var(--blue-dark));
    border-radius: 58px;
  }

  .star-magnets { position: absolute; left: 180px; top: 540px; }

  .note {
    position: absolute; color: var(--note);
    font-family: "Roboto", sans-serif; font-size: 18px;
  }
  .note-stars { left: 158px; top: 499px; }
  .note-words { left: 69px; top: 864px; }
  .leader { position: absolute; left: 0; top: 0; }

  .word-magnet {
    position: absolute; width: 277px; height: 79px;
    box-shadow: 7px 7px 0 var(--shadow);
    border-radius: 0 14px 14px 0;
  }
  .word-magnet .magnet-border {
    position: absolute; inset: 0;
    background: linear-gradient(90deg, var(--coral), var(--yellow) 50%, var(--coral));
  }
  .word-magnet .value {
    position: absolute; left: 13px; right: 13px; top: 14px; bottom: 14px;
    background: var(--white);
    display: flex; align-items: center; justify-content: center;
    color: var(--navy); font-weight: 800; font-size: 31px; letter-spacing: 0.3px;
    white-space: nowrap;
  }
  .col-1 { left: 109px; } .col-2 { left: 401px; } .col-3 { left: 693px; }
  .row-1 { top: 933px; } .row-2 { top: 1034px; }
</style>
</head>
<body>

<section class="board">
  <div class="board-frame" role="img" aria-label="Border of geometric tiles in navy, light blue and yellow"></div>
  <div class="title-field"></div>
  <h1 class="board-title"><span class="name">TAVRON</span><span class="sub">OF THE MONTH</span></h1>
  <div class="thermometer" role="img" aria-label="Thermometer illustration in light and dark blue with cream fill"></div>
</section>

<svg class="leader" width="1087" height="1200" aria-hidden="true">
  <line x1="223" y1="525" x2="245" y2="600" stroke="var(--note)" stroke-width="0.8"/>
  <line x1="81" y1="897" x2="103" y2="972" stroke="var(--note)" stroke-width="0.8"/>
</svg>

<p class="note note-stars">star shape magnets</p>
<p class="note note-words">word magnets</p>

<svg class="star-magnets" width="220" height="170" viewBox="0 0 220 170" aria-label="Star shape magnets">
  <defs>
    <polygon id="star" points="38,0 26.8,11.1 26.9,26.9 11.1,26.8 0,38 -11.1,26.8 -26.9,26.9 -26.8,11.1 -38,0 -26.8,-11.1 -26.9,-26.9 -11.1,-26.8 0,-38 11.1,-26.8 26.9,-26.9 26.8,-11.1"/>
  </defs>
  <g transform="translate(124 54) rotate(10)"><use href="#star" fill="var(--shadow)"/></g>
  <g transform="translate(120 50) rotate(10)"><use href="#star" fill="var(--blue-light)"/></g>
  <g transform="translate(57 117)"><use href="#star" fill="var(--shadow)"/></g>
  <g transform="translate(53 113)"><use href="#star" fill="var(--coral)"/></g>
  <g transform="translate(172 124) rotate(-8)"><use href="#star" fill="var(--shadow)"/></g>
  <g transform="translate(168 120) rotate(-8)"><use href="#star" fill="var(--yellow)"/></g>
</svg>

<div class="word-magnet col-1 row-1"><div class="magnet-border" role="img" aria-label="Coral and yellow triangle pattern border"></div><span class="value">SIMPLICITY</span></div>
<div class="word-magnet col-2 row-1"><div class="magnet-border" role="img" aria-label="Coral and yellow triangle pattern border"></div><span class="value">INTEGRITY</span></div>
<div class="word-magnet col-3 row-1"><div class="magnet-border" role="img" aria-label="Coral and yellow triangle pattern border"></div><span class="value">STEWARDSHIP</span></div>
<div class="word-magnet col-1 row-2"><div class="magnet-border" role="img" aria-label="Coral and yellow triangle pattern border"></div><span class="value">PEACE</span></div>
<div class="word-magnet col-2 row-2"><div class="magnet-border" role="img" aria-label="Coral and yellow triangle pattern border"></div><span class="value">EQUALITY</span></div>
<div class="word-magnet col-3 row-2"><div class="magnet-border" role="img" aria-label="Coral and yellow triangle pattern border"></div><span class="value">COMMUNITY</span></div>

</body>
</html>
```